Business cards, e-mail signature, letterhead
Noral Studio, Inc
Business cards, e-mail signature, letterhead - Communications and Media
Creative Brief
Bright & Fun-filled
Tobin Varley
President, Noral Studio Inc.
Card: New York City Letterhead: 47 West 112th St. 9F New York, NY 10031
skype: tobinvarley604
tbnvrl@quillpost.net
www.NoralStudio.com
Locations of our properties can be listed on the back of card (see below) and incorporated into letterhead.
Ash Fork, AZ / Ashtabula, OH/ Belle Rose, LA/ Blanca, CO/ Cross City, FL/ Dulac, LA/ Huntington, OR/ Islamorada, FL/ Lead, SD/ Mona, UT/ Morgan, GA/ Ty Ty, GA/ Winchester, VA

```html
<!DOCTYPE html>
<html lang="en">
<head>
<meta charset="utf-8">
<title>Noral Studio, Inc — Business Cards</title>
<link rel="stylesheet" href="https://fonts.googleapis.com/css2?family=Montserrat:wght@400;500;700;800&family=Open+Sans:wght@400;600&display=swap">
<style>
  :root{
    --bg:#e9eaee;
    --card:#ffffff;
    --navy:#23276b;
    --indigo:#3a3f9c;
    --violet:#5a5fc4;
    --grey:#8b8e96;
    --ink:#4a4d55;
    --rule:#d4d6dc;
  }
  *{box-sizing:border-box;margin:0;padding:0}
  html,body{width:1200px;height:1006px;overflow:hidden;background:var(--bg)}
  body{font-family:"Open Sans",Arial,sans-serif;color:var(--ink);position:relative}

  .card{
    position:absolute;left:220px;width:760px;height:434px;
    background:var(--card);border-radius:26px;overflow:hidden;
    box-shadow:0 10px 30px rgba(30,32,70,.16);
  }
  .card--front{top:46px}
  .card--back{top:526px}

  /* front */
  .brand{position:absolute;left:56px;top:52px;display:flex;align-items:center;gap:20px}
  .brand__dot{width:78px;height:78px;border-radius:50%;background:var(--navy)}
  .brand__name{font-family:"Montserrat",Arial,sans-serif;font-weight:800;font-size:34px;color:var(--navy);letter-spacing:.5px;line-height:1}
  .brand__tag{font-family:"Montserrat",Arial,sans-serif;font-size:15px;color:var(--grey);letter-spacing:3px;margin-top:8px;padding-left:40px}

  .contacts{position:absolute;left:56px;top:176px;list-style:none}
  .contacts li{display:flex;align-items:center;gap:12px;font-size:14px;line-height:1.25;margin-bottom:9px;color:var(--ink)}
  .contacts svg{flex:none;width:20px;height:20px}

  .signer{position:absolute;right:56px;top:300px;text-align:right}
  .signer__name{font-family:"Montserrat",Arial,sans-serif;font-weight:700;font-size:17px;color:var(--navy)}
  .signer__role{font-size:13px;color:var(--grey);margin-top:2px}

  .band{position:absolute;left:0;bottom:0;width:760px;height:90px}
  .band__url{position:absolute;right:56px;bottom:24px;font-family:"Montserrat",Arial,sans-serif;font-size:15px;letter-spacing:2px;color:#fff}

  /* back */
  .back-brand{position:absolute;left:0;right:0;top:140px;display:flex;flex-direction:column;align-items:center;gap:18px}
  .back-brand__dot{width:110px;height:110px;border-radius:50%;background:var(--navy)}
  .back-brand__name{font-family:"Montserrat",Arial,sans-serif;font-weight:800;font-size:26px;color:var(--navy);letter-spacing:.5px}
  .back-url{position:absolute;left:56px;bottom:40px;font-family:"Montserrat",Arial,sans-serif;font-size:15px;letter-spacing:2px;color:var(--ink)}
</style>
</head>
<body>

<section class="card card--front">
  <div class="brand">
    <span class="brand__dot"></span>
    <div>
      <div class="brand__name">NORAL STUDIO INC.</div>
      <div class="brand__tag">Sound...Refined</div>
    </div>
  </div>

  <ul class="contacts">
    <li>
      <svg viewBox="0 0 20 20"><circle cx="10" cy="10" r="10" fill="#23276b"/><path d="M10 4.5a3.5 3.5 0 0 0-3.5 3.5c0 2.6 3.5 7 3.5 7s3.5-4.4 3.5-7A3.5 3.5 0 0 0 10 4.5zm0 4.8a1.3 1.3 0 1 1 0-2.6 1.3 1.3 0 0 1 0 2.6z" fill="#fff"/></svg>
      <span>47 West 112th St. 9F<br>New York, NY 10031</span>
    </li>
    <li>
      <svg viewBox="0 0 20 20"><circle cx="10" cy="10" r="10" fill="#23276b"/><path d="M7 5l2 2.6-1.1 1.3a6.5 6.5 0 0 0 3.2 3.2l1.3-1.1L15 13l-.7 1.6c-4.3.3-8.6-4-8.3-8.3z" fill="#fff"/></svg>
      <span>(604) 555-0172</span>
    </li>
    <li>
      <svg viewBox="0 0 20 20"><circle cx="10" cy="10" r="10" fill="#23276b"/><path d="M5 6h10v6.5H9l-2.5 2v-2H5z" fill="#fff"/></svg>
      <span>tobinvarley604</span>
    </li>
    <li>
      <svg viewBox="0 0 20 20"><circle cx="10" cy="10" r="10" fill="#23276b"/><rect x="5" y="6.5" width="10" height="7" fill="#fff"/><path d="M5 6.5l5 4 5-4" stroke="#23276b" stroke-width="1" fill="none"/></svg>
      <span>tbnvrl@quillpost.net</span>
    </li>
    <li>
      <svg viewBox="0 0 20 20"><circle cx="10" cy="10" r="10" fill="#23276b"/><g fill="none" stroke="#fff" stroke-width="1.1"><circle cx="10" cy="10" r="5"/><ellipse cx="10" cy="10" rx="2.2" ry="5"/><path d="M5 10h10"/></g></svg>
      <span>www.NoralStudio.com</span>
    </li>
  </ul>

  <div class="signer">
    <div class="signer__name">Tobin Varley</div>
    <div class="signer__role">President, Noral Studio Inc.</div>
  </div>

  <svg class="band" viewBox="0 0 760 90" preserveAspectRatio="none">
    <defs>
      <linearGradient id="bandFill" x1="0" y1="0" x2="1" y2="0">
        <stop offset="0" stop-color="#23276b"/>
        <stop offset=".55" stop-color="#3a3f9c"/>
        <stop offset="1" stop-color="#5a5fc4"/>
      </linearGradient>
    </defs>
    <path d="M0 48 C 180 48 230 48 300 48 C 360 48 360 14 420 14 L 760 14 L 760 90 L 0 90 Z" fill="#c9cbd3"/>
    <path d="M0 56 C 200 56 250 56 310 56 C 370 56 370 22 430 22 L 760 22 L 760 90 L 0 90 Z" fill="url(#bandFill)"/>
  </svg>
  <div class="band__url">www.NoralStudio.com</div>
</section>

<section class="card card--back">
  <div class="back-brand">
    <span class="back-brand__dot"></span>
    <div class="back-brand__name">Noral Studio Inc.</div>
  </div>
  <div class="back-url">www.NoralStudio.com</div>
</section>

</body>
</html>
```